Vascular Secialist needs a tri-fold brochure

I would like to create a tri- fold of all the services that the vascular practice offers. The practice specializes in lower extremity vascular diseases. I would like to have the tri-fold have brief descriptions of all the services as well as images of the practice to show case the top of the line technology. The trip-fold will be front in back with a crisp modern design. The diseases that they treat are: arterial disease, venous disease, varicose veins, chronic venous insufficiency, deep vein thrombosis, uterine fibroids, pelvic and labial varicose veins, varicocele. Treatment options for all diseases that the practice treats.

Target Market(s)

Doctors

Industry/Entity Type

Medical

Other font styles liked:
• Myriod Pro SemiExtende

Colors
33a6d7
86cae7
aaaaaa
85cae6
dcedf6
cee9f5
757575
9d9d9d
c3c3c3

Requirements
Must have
• creativity and taglines that capture the reader
Nice to have
• I would like the piece to mirror the website. www.lumavexclinic.example

```html
<!DOCTYPE html>
<html lang="en">
<head>
<meta charset="utf-8">
<title>Lumavex Clinic – Tri-fold Brochure</title>
<link rel="stylesheet" href="https://fonts.googleapis.com/css2?family=Oswald:wght@500;700&family=Open+Sans:wght@400;600;700&display=swap">
<style>
  :root{
    --blue:#33a6d7;
    --blue-bright:#3cb4e8;
    --blue-soft:#86cae7;
    --ice:#dcedf6;
    --dark:#4a4a4c;
    --ink:#2b3a44;
    --grey:#757575;
    --light:#f2f4f5;
    --white:#ffffff;
    --bg:#e9eef1;
  }
  *{box-sizing:border-box;margin:0;padding:0}
  html,body{width:1200px;height:1200px;overflow:hidden;background:var(--bg)}
  body{font-family:"Open Sans",Arial,sans-serif;color:var(--ink)}
  .brochure{position:absolute;left:30px;top:210px;width:1140px;height:780px;background:var(--white);box-shadow:0 10px 30px rgba(0,0,0,.18);overflow:hidden}
  .shapes{position:absolute;left:0;top:0}
  .fold{position:absolute;top:0;bottom:0;width:1px;background:rgba(0,0,0,.08)}
  .abs{position:absolute}

  /* panel 1 */
  .about-bar{left:0;top:30px;width:360px;height:44px;background:var(--dark);color:var(--white);font-size:22px;font-weight:600;padding:8px 0 0 24px}
  .about-text{left:24px;top:92px;width:330px;font-size:12.5px;line-height:1.6;color:var(--ink)}
  .badge{left:228px;top:262px;width:146px;height:146px;border-radius:50%;background:var(--white);border:5px solid var(--blue);box-shadow:0 4px 12px rgba(0,0,0,.25);display:flex;flex-direction:column;align-items:center;justify-content:center;font-family:"Oswald",sans-serif;font-weight:700;line-height:1}
  .badge .t1{font-size:27px;color:var(--dark)}
  .badge .t2{font-size:27px;color:var(--blue)}
  .disease-list{left:30px;top:430px;list-style:none;color:var(--white);font-size:16px}
  .disease-list li{display:flex;align-items:center;gap:12px;height:32px}

  /* panel 2 */
  .phys-bg{left:380px;top:0;width:380px;height:470px;background:linear-gradient(180deg,var(--light),#ffffff)}
  .phys-title{left:410px;top:34px;font-size:30px;line-height:1.05;color:var(--blue);font-weight:400}
  .portrait{width:104px;height:104px;border-radius:50%;border:5px solid var(--blue-soft);background:radial-gradient(circle at 50% 40%,#d9b89c,#8fa7b8 70%);box-shadow:0 3px 8px rgba(0,0,0,.2)}
  .doc-name{width:180px;text-align:center;font-size:11.5px;font-weight:600;color:var(--ink);line-height:1.35}
  .doc-name span{display:block;font-weight:400;font-style:italic;color:var(--blue)}
  .contact{left:410px;top:505px;width:330px}
  .contact h3{font-family:"Oswald",sans-serif;font-weight:700;font-size:28px;line-height:1.1;color:var(--ink);margin-bottom:10px}
  .contact p{display:flex;gap:10px;align-items:flex-start;font-size:13.5px;line-height:1.45;margin-bottom:4px;font-weight:600}
  .contact svg{flex:none;margin-top:2px}

  /* panel 3 */
  .brand{left:820px;top:40px;display:flex;align-items:center;gap:12px;font-size:34px;font-weight:400;letter-spacing:3px;color:var(--dark)}
  .brand i{width:24px;height:24px;border-radius:50%;background:var(--dark);display:block}
  .hero-photo{left:760px;top:120px;width:380px;height:420px;background:linear-gradient(160deg,#f4f6f7 0%,#e6ecef 55%,#c9d3d9 100%)}
  .headline{left:790px;top:545px;width:330px;font-family:"Oswald",sans-serif;font-weight:700;font-size:28px;line-height:1.12;color:var(--white)}
  .headline .dark{color:var(--ink)}
</style>
</head>
<body>
<main class="brochure">
  <div class="phys-bg abs"></div>
  <div class="hero-photo abs" role="img" aria-label="Photo of a smiling senior physician in a white coat with a stethoscope"></div>

  <svg class="shapes" width="1140" height="780" viewBox="0 0 1140 780" aria-hidden="true">
    <path d="M0 280 C140 290 290 330 380 470 L380 710 L0 710 Z" fill="var(--blue-bright)"/>
    <path d="M0 280 C140 290 290 330 380 470" fill="none" stroke="var(--blue-soft)" stroke-width="6"/>
    <path d="M380 470 C470 482 620 492 760 500" fill="none" stroke="var(--blue-soft)" stroke-width="4"/>
    <rect x="380" y="682" width="380" height="28" fill="var(--blue-bright)"/>
    <path d="M760 500 C900 540 1040 545 1140 510 L1140 710 L760 710 Z" fill="var(--blue)"/>
    <path d="M760 500 C900 540 1040 545 1140 510" fill="none" stroke="var(--white)" stroke-width="8"/>
    <rect x="0" y="710" width="1140" height="70" fill="var(--dark)"/>
  </svg>

  <div class="fold" style="left:380px"></div>
  <div class="fold" style="left:760px"></div>

  <!-- Panel 1 -->
  <div class="about-bar abs">About Us</div>
  <p class="about-text abs">The physicians at our clinic have devoted their lives to saving limbs and easing the pain caused by vascular disease. Our modern facility uses the latest minimally invasive treatments in a calm, welcoming setting. Our friendly staff members make every visit smooth and efficient, so you leave feeling informed, confident and cared for, free to enjoy the little things in life that matter most to you.</p>
  <div class="badge abs"><span class="t1">DISEASES</span><span class="t2">WE TREAT</span></div>
  <ul class="disease-list abs">
    <li><svg width="18" height="14" viewBox="0 0 18 14"><path d="M2 7 L7 12 L16 2" fill="none" stroke="var(--ink)" stroke-width="2.5"/></svg>Arterial disease</li>
    <li><svg width="18" height="14" viewBox="0 0 18 14"><path d="M2 7 L7 12 L16 2" fill="none" stroke="var(--ink)" stroke-width="2.5"/></svg>Venous disease</li>
    <li><svg width="18" height="14" viewBox="0 0 18 14"><path d="M2 7 L7 12 L16 2" fill="none" stroke="var(--ink)" stroke-width="2.5"/></svg>Varicose veins</li>
    <li><svg width="18" height="14" viewBox="0 0 18 14"><path d="M2 7 L7 12 L16 2" fill="none" stroke="var(--ink)" stroke-width="2.5"/></svg>Chronic venous insufficiency</li>
    <li><svg width="18" height="14" viewBox="0 0 18 14"><path d="M2 7 L7 12 L16 2" fill="none" stroke="var(--ink)" stroke-width="2.5"/></svg>Deep vein thrombosis</li>
    <li><svg width="18" height="14" viewBox="0 0 18 14"><path d="M2 7 L7 12 L16 2" fill="none" stroke="var(--ink)" stroke-width="2.5"/></svg>Uterine fibroids</li>
    <li><svg width="18" height="14" viewBox="0 0 18 14"><path d="M2 7 L7 12 L16 2" fill="none" stroke="var(--ink)" stroke-width="2.5"/></svg>Pelvic and labial varicose veins</li>
    <li><svg width="18" height="14" viewBox="0 0 18 14"><path d="M2 7 L7 12 L16 2" fill="none" stroke="var(--ink)" stroke-width="2.5"/></svg>Varicocele</li>
  </ul>

  <!-- Panel 2 -->
  <h2 class="phys-title abs">Our<br>Physicians</h2>
  <div class="portrait abs" style="left:418px;top:120px" role="img" aria-label="Portrait photo of Dr. Maren Okafor"></div>
  <div class="doc-name abs" style="left:380px;top:234px">Maren Okafor, M.D., F.A.C.S.<span>Vascular Specialist</span></div>
  <div class="portrait abs" style="left:618px;top:100px" role="img" aria-label="Portrait photo of Dr. Tobias Reyes"></div>
  <div class="doc-name abs" style="left:580px;top:214px">Tobias Reyes, M.D.<span>Vascular Specialist</span></div>
  <div class="portrait abs" style="left:528px;top:290px" role="img" aria-label="Portrait photo of Dr. Daniel Ashby"></div>
  <div class="doc-name abs" style="left:490px;top:404px">Daniel Ashby, M.D.<span>Vascular Specialist</span></div>

  <div class="contact abs">
    <h3>CONTACT US</h3>
    <p><svg width="16" height="16" viewBox="0 0 16 16"><circle cx="8" cy="8" r="8" fill="var(--ink)"/><path d="M8 3.5a3 3 0 0 1 3 3c0 2.2-3 5.5-3 5.5S5 8.7 5 6.5a3 3 0 0 1 3-3z" fill="#fff"/></svg>1820 Harbor Crest Lane<br>Seaview, CA 90000</p>
    <p><svg width="16" height="16" viewBox="0 0 16 16"><circle cx="8" cy="8" r="8" fill="var(--ink)"/><path d="M5 4l2 0 .6 2-1 .8a5 5 0 0 0 2.6 2.6l.8-1 2 .6 0 2c-4 .4-7.4-3-7-7z" fill="#fff"/></svg>(555) 014-2270</p>
    <p><svg width="16" height="16" viewBox="0 0 16 16"><circle cx="8" cy="8" r="8" fill="var(--ink)"/><path d="M5 4l2 0 .6 2-1 .8a5 5 0 0 0 2.6 2.6l.8-1 2 .6 0 2c-4 .4-7.4-3-7-7z" fill="#fff"/></svg>(555) 014-3981</p>
    <p><svg width="16" height="16" viewBox="0 0 16 16"><circle cx="8" cy="8" r="8" fill="var(--ink)"/><circle cx="8" cy="8" r="4" fill="none" stroke="#fff" stroke-width="1.3"/><path d="M4 8h8M8 4v8" stroke="#fff" stroke-width="1"/></svg>www.lumavexclinic.example</p>
  </div>

  <!-- Panel 3 -->
  <div class="brand abs"><i></i>LUMAVEX</div>
  <h1 class="headline abs">The Leading Vascular Surgery Facility for <span class="dark">Treating Arterial Disease and Venous Disease</span></h1>
</main>
</body>
</html>
```